Quorvane Capital Modern Business Card

We need a modern business card template designed for Quorvane Capital.
Quorvane Capital is a diversified global cryptocurrency investment fund.

The font under the logo: Hiragino Kaku Gothic Pro

Color Hexcode: Main colors white (ffffff) & teal (188383), we are open to adding #fcca46 as an accent

Target Market(s)

Accredited Investors, high net worth individuals and institutional investors

Industry/Entity Type

Investment

Contact Information for Business Card

Contact Information should contain
Name
main phone +1 720 555 0147
cell
email

Font styles to use
Sans Serif
Other font styles liked:
• Hiragino Kaku Gothic Pro

Requirements
Must have
• would like to have icons that identify the contact information
• include our website: www.quorvanecapital.example
• include our Tagline: Diversified Crypto Investment Funds
Nice to have
• Would like to have a simple back side with the logo (without the words) and plenty of space

```html
<!DOCTYPE html>
<html lang="en">
<head>
<meta charset="utf-8">
<title>Quorvane Capital — Business Card</title>
<link rel="stylesheet" href="https://fonts.googleapis.com/css2?family=Fira+Sans:wght@500&family=Work+Sans:wght@400&family=Noto+Sans+JP:wght@300&display=swap">
<style>
  :root {
    --backdrop: #161616;
    --card: #212121;
    --card-light: #333333;
    --teal: #188383;
    --teal-bright: #2a9a98;
    --white: #ffffff;
    --text: #e9e9e9;
    --muted: #8c8c8c;
  }
  * { margin: 0; padding: 0; box-sizing: border-box; }
  html, body {
    width: 1200px; height: 897px; overflow: hidden;
    background: var(--backdrop);
  }
  .canvas { position: relative; width: 1200px; height: 897px; }

  .card {
    position: absolute; left: 304px; width: 594px; height: 338px;
    border-radius: 22px;
    background: radial-gradient(ellipse 60% 70% at 82% 45%, var(--card-light), var(--card) 75%);
    box-shadow: 0 6px 14px rgba(0,0,0,.55);
  }
  .card--front { top: 92px; }
  .card--back  { top: 470px; }

  .brand {
    position: absolute; left: 36px; width: 250px; top: 226px;
    display: flex; flex-direction: column; align-items: center;
  }
  .brand__row { display: flex; align-items: center; gap: 9px; }
  .brand__square { width: 12px; height: 12px; background: var(--teal-bright); }
  .brand__name {
    font-family: "Noto Sans JP", sans-serif; font-weight: 300;
    font-size: 21px; line-height: 26px; letter-spacing: .2px; color: var(--white);
    text-transform: uppercase; white-space: nowrap;
  }
  .brand__tagline {
    margin-top: 6px;
    font-family: "Work Sans", sans-serif; font-size: 11px; line-height: 14px;
    letter-spacing: .6px; color: var(--teal-bright); white-space: nowrap;
  }

  .divider {
    position: absolute; left: 296px; top: 88px; width: 2px; height: 164px;
    background: var(--teal-bright);
  }

  .details { position: absolute; left: 329px; top: 84px; font-family: "Work Sans", sans-serif; color: var(--text); }
  .details__name {
    font-family: "Fira Sans", sans-serif; font-weight: 500;
    font-size: 20px; letter-spacing: .8px; color: var(--teal-bright);
    text-transform: uppercase; line-height: 24px;
  }
  .details__title { font-size: 14px; line-height: 18px; margin-top: 2px; letter-spacing: .3px; }
  .details__company {
    font-family: "Fira Sans", sans-serif; font-weight: 500;
    font-size: 16.5px; letter-spacing: .5px; color: var(--teal-bright);
    text-transform: uppercase; margin-top: 10px; line-height: 20px;
  }
  .details__address { font-size: 13.5px; line-height: 17px; letter-spacing: .3px; }
  .contact { list-style: none; margin-top: 9px; }
  .contact__item {
    display: flex; align-items: center; gap: 9px;
    font-size: 13.5px; line-height: 19px; letter-spacing: .4px; white-space: nowrap;
  }
  .contact__icon { width: 12px; height: 12px; flex: none; margin-left: 2px; }
  .contact__icon--solid { fill: var(--teal-bright); }
  .contact__icon--line { fill: none; stroke: var(--teal-bright); stroke-width: 2; }

  .back__name {
    position: absolute; left: 0; right: 0; top: 233px; text-align: center;
    font-family: "Noto Sans JP", sans-serif; font-weight: 300;
    font-size: 26px; line-height: 34px; color: var(--muted);
    text-transform: uppercase; letter-spacing: .3px;
  }
</style>
</head>
<body>
<main class="canvas">
  <section class="card card--front">
    <div class="brand">
      <div class="brand__row">
        <span class="brand__square"></span>
        <span class="brand__name">Quorvane Capital</span>
      </div>
      <p class="brand__tagline">Diversified Crypto Investment Funds</p>
    </div>
    <div class="divider"></div>
    <div class="details">
      <p class="details__name">Dorian Velsmark</p>
      <p class="details__title">Managing Director</p>
      <p class="details__company">Quorvane Capital</p>
      <p class="details__address">48 Larkmoor Avenue, Suite<br>3/B, Fenwick</p>
      <ul class="contact">
        <li class="contact__item">
          <svg class="contact__icon contact__icon--solid" viewBox="0 0 24 24"><path d="M6.6 10.8a15.1 15.1 0 0 0 6.6 6.6l2.2-2.2a1 1 0 0 1 1-.25 11.4 11.4 0 0 0 3.6.57 1 1 0 0 1 1 1V20a1 1 0 0 1-1 1A17 17 0 0 1 3 4a1 1 0 0 1 1-1h3.5a1 1 0 0 1 1 1c0 1.25.2 2.45.57 3.57a1 1 0 0 1-.25 1z"/></svg>
          <span>+1 720 555 0147</span>
        </li>
        <li class="contact__item">
          <svg class="contact__icon contact__icon--line" viewBox="0 0 24 24"><rect x="6" y="2" width="12" height="20" rx="2"/><path d="M10.5 18h3"/></svg>
          <span>+1 720 555 0147</span>
        </li>
        <li class="contact__item">
          <svg class="contact__icon contact__icon--line" viewBox="0 0 24 24"><rect x="2" y="5" width="20" height="14" rx="1"/><path d="M2.5 6 12 13l9.5-7"/></svg>
          <span>info@quorvanecapital.example</span>
        </li>
        <li class="contact__item">
          <svg class="contact__icon contact__icon--line" viewBox="0 0 24 24"><circle cx="12" cy="12" r="9.5"/><ellipse cx="12" cy="12" rx="4" ry="9.5"/><path d="M2.5 12h19"/></svg>
          <span>www.quorvanecapital.example</span>
        </li>
      </ul>
    </div>
  </section>

  <section class="card card--back">
    <p class="back__name">Quorvane Capital</p>
  </section>
</main>
</body>
</html>
```